Criação de Manual da Marca para Viagens & Lazer
A empresa queria:
" Funciona como o uBodal, mas para festas em geral, incluindo festas de pets. O responsável pela festa se cadastra, escolhe o tipo de festa (adulto, teen, infantil, chá de bebê, etc), insere as informações da festa e lança o site no ar. Acoplado a ele está uma lista de presentes ilustrada por produtos reais adequados ao tipo de festa e faixa etária do evento que são conversíveis em créditos. Não há entrega de produto, o total arrecadado é depositado na conta do cliente ou da instituição de caridade por ele indicada. "

```html
<!DOCTYPE html>
<html lang="pt-BR">
<head>
<meta charset="UTF-8">
<title>Manual da Marca — Logomarca — Redução</title>
<link href="https://fonts.googleapis.com/css2?family=Cabin:wght@400;500;600&display=swap" rel="stylesheet">
<style>
  :root {
    --backdrop: #e6e6e6;
    --page: #ffffff;
    --ink: #3a3a3a;
    --ink-soft: #6b6b6b;
    --accent: #e8541e;
    --rule-start: #f2a33a;
    --rule-end: #e58aa8;
    --measure: #3ab6e0;
    --watermark: #fbeeee;
  }
  * { margin: 0; padding: 0; box-sizing: border-box; }
  html, body { width: 1200px; height: 1200px; overflow: hidden; }
  body {
    background: var(--backdrop);
    font-family: "Cabin", sans-serif;
    color: var(--ink);
  }
  .manual-page {
    position: absolute;
    left: 60px; top: 60px;
    width: 1080px; height: 1080px;
    background: var(--page);
    box-shadow: 0 10px 40px rgba(0,0,0,.18);
    overflow: hidden;
  }
  .watermark-shape {
    position: absolute;
    left: 420px; top: 140px;
    width: 620px; height: 700px;
    background: var(--watermark);
    border-radius: 40px;
  }
  .page-header {
    position: absolute;
    left: 27px; right: 27px; top: 70px;
    display: flex; justify-content: space-between;
    font-size: 33px; font-weight: 500; letter-spacing: .5px;
  }
  .header-rule {
    position: absolute;
    left: 27px; right: 0; top: 112px;
    height: 3px;
    background: linear-gradient(90deg, var(--rule-start), var(--rule-end));
  }
  .section-title {
    position: absolute; left: 27px; top: 150px;
    font-size: 46px; font-weight: 400; color: var(--ink-soft); letter-spacing: 1px;
  }
  .subsection-title {
    position: absolute; left: 27px; top: 250px;
    font-size: 21px; font-weight: 500; letter-spacing: .5px;
  }
  .body-copy {
    position: absolute;
    font-size: 20px; line-height: 1.3; color: var(--ink);
  }
  .body-copy.intro { left: 27px; top: 305px; width: 300px; }
  .body-copy.spec { left: 377px; top: 250px; width: 330px; }
  .logo-tile {
    position: absolute;
    display: flex; align-items: center; justify-content: center;
    background: var(--accent);
    color: #ffffff;
    font-weight: 600;
    white-space: nowrap;
  }
  .tile-xl { left: 27px;  top: 606px; width: 183px; height: 168px; font-size: 30px; }
  .tile-lg { left: 320px; top: 655px; width: 115px; height: 106px; font-size: 19px; }
  .tile-md { left: 494px; top: 690px; width: 66px;  height: 61px;  font-size: 11px; }
  .tile-sm { left: 642px; top: 722px; width: 46px;  height: 43px;  font-size: 8px; }
  .tile-xs { left: 765px; top: 741px; width: 30px;  height: 28px;  font-size: 5px; }
  .size-measure { position: absolute; left: 800px; top: 736px; width: 160px; height: 40px; }
  .measure-label {
    position: absolute; font-size: 12px; color: var(--ink-soft); white-space: nowrap;
  }
  .measure-label.print { left: 40px; top: 4px; }
  .measure-label.digital { left: 18px; top: 24px; }
  .footer-note {
    position: absolute; left: 45px; top: 896px;
    font-size: 18px; line-height: 1.3; font-weight: 500; letter-spacing: .3px;
  }
</style>
</head>
<body>
  <main class="manual-page">
    <div class="watermark-shape" aria-hidden="true"></div>

    <header class="page-header">
      <span>LOGOMARCA</span>
      <span>REDUÇÃO</span>
    </header>
    <div class="header-rule"></div>

    <h1 class="section-title">REDUÇÃO</h1>
    <h2 class="subsection-title">DIMENSÃO MÍNIMA</h2>

    <p class="body-copy intro">A dimensão mínima preserva a legibilidade da logomarca e tem a medida estipulada ao lado.</p>
    <p class="body-copy spec">Para impressão em materiais gráficos em geral, a dimensão mínima é de 12 px em ambientes digitais ou 0,42 x 0,35 cm em impressos, tendo como referência a altura do lettering “FB” da logomarca.</p>

    <div class="logo-tile tile-xl">Festa Box</div>
    <div class="logo-tile tile-lg">Festa Box</div>
    <div class="logo-tile tile-md">Festa Box</div>
    <div class="logo-tile tile-sm">Festa Box</div>
    <div class="logo-tile tile-xs">Festa Box</div>

    <div class="size-measure">
      <svg width="40" height="30" viewBox="0 0 40 30" aria-hidden="true">
        <rect x="8" y="4" width="6" height="18" fill="var(--measure)"/>
        <line x1="2" y1="4" x2="20" y2="4" stroke="#999" stroke-width="1"/>
        <line x1="2" y1="22" x2="20" y2="22" stroke="#999" stroke-width="1"/>
        <line x1="20" y1="13" x2="36" y2="13" stroke="#999" stroke-width="1"/>
      </svg>
      <span class="measure-label print">0,42 X 0,35CM</span>
      <span class="measure-label digital">12PX</span>
    </div>

    <p class="footer-note">AS DIRETRIZES DE REDUÇÃO MÍNIMA<br>VALEM PARA TODAS VERSÕES DA LOGOMARCA.</p>
  </main>
</body>
</html>
```